training slide

We have an existing PPT template.

I am just looking for someone to make the attached slides better looking. If that goes well we have a whole bunch of presentations that need formatting in a similar style. Our customer base is made up of pharmaceutical and healthcare companies. we charge high end consultancy prices and it is very important our production value reflects this level of quality. We are not attached to the current PPT template and if anyone wants to re-visit that we would be very keen to see any ideas. We do however like our kelOrvanta logo but you can lose the energy, experience etc.

Industry/Entity Type

Training

```html
<!DOCTYPE html>
<html lang="en">
<head>
<meta charset="utf-8">
<title>kelOrvanta – Training Slides</title>
<link href="https://fonts.googleapis.com/css2?family=Open+Sans:ital,wght@0,400;0,600;0,700;1,400&family=Tinos:ital,wght@1,700&display=swap" rel="stylesheet">
<style>
  :root {
    --plum: #5c0f46;
    --magenta: #e0339b;
    --pink-text: #e0208c;
    --ink: #222222;
    --muted: #555555;
    --white: #ffffff;
    --grey-wave: #d9d9d9;
    --backdrop: #efe9e2;
    --energy: #a0449a;
    --credibility: #3a4a9c;
    --relationships: #f26a22;
  }
  * { box-sizing: border-box; margin: 0; padding: 0; }
  html, body { width: 1200px; height: 591px; overflow: hidden; }
  body {
    background: var(--backdrop);
    font-family: "Open Sans", Arial, sans-serif;
    color: var(--ink);
    position: relative;
  }
  .slide {
    position: absolute;
    width: 342px;
    height: 257px;
    background: var(--white);
    overflow: hidden;
    box-shadow: 0 1px 4px rgba(0,0,0,0.25);
  }
  .slide--r1 { top: 32px; }
  .slide--r2 { top: 307px; }
  .slide--c1 { left: 42px; }
  .slide--c2 { left: 433px; }
  .slide--c3 { left: 828px; }

  .slide-header {
    position: absolute; top: 0; left: 0; right: 0; height: 35px;
    background: linear-gradient(90deg, var(--plum) 0%, #8e1a6a 40%, var(--magenta) 100%);
    display: flex; align-items: center; justify-content: space-between;
    padding: 0 8px 0 10px; color: var(--white);
  }
  .slide-title { font-size: 14px; font-weight: 700; }
  .brand-strip { display: flex; align-items: center; gap: 6px; font-size: 6.5px; font-weight: 700; }
  .brand-name { font-size: 10px; font-weight: 600; }

  .slide-footer { position: absolute; left: 0; bottom: 0; width: 342px; height: 60px; }
  .footer-text {
    position: absolute; left: 10px; right: 14px; bottom: 6px;
    display: flex; justify-content: space-between;
    font-size: 6.5px; color: var(--white);
  }
  .footer-url { letter-spacing: 1.6px; }

  .slide--cover {
    background: radial-gradient(ellipse at 50% 42%, #e0399f 0%, #b5217f 40%, #6a0f50 100%);
    color: var(--white); text-align: center;
  }
  .cover-brand { position: absolute; top: 76px; width: 100%; font-size: 22px; font-weight: 600; }
  .cover-tagline { position: absolute; top: 108px; width: 100%; font-size: 8.5px; font-weight: 700; }
  .cover-name { position: absolute; top: 136px; width: 100%; font-size: 14px; font-weight: 700; }
  .cover-date { position: absolute; top: 157px; width: 100%; font-size: 13px; }

  .tick-list { position: absolute; list-style: none; font-size: 12px; }
  .tick-list li { display: flex; align-items: flex-start; gap: 5px; line-height: 1.25; }
  .tick { flex: none; width: 9px; height: 9px; margin-top: 3px; }
  .tick-list--profile { left: 18px; top: 53px; }
  .tick-list--profile li + li { margin-top: 20px; }
  .tick-list--proposition { left: 96px; top: 92px; }
  .tick-list--proposition li + li { margin-top: 16px; }
  .tick-list--proposition li:nth-child(2), .tick-list--proposition li:nth-child(3) { margin-left: 10px; }

  .mission-text {
    position: absolute; top: 107px; left: 0; right: 0;
    text-align: center; font-size: 12px; line-height: 19px;
  }

  .value-card { position: absolute; color: var(--white); padding: 4px 0 0 10px; }
  .value-card h3 { font-size: 11.5px; font-weight: 700; margin-bottom: 2px; }
  .value-card ul { list-style: none; font-size: 7px; line-height: 12px; }
  .value-card li::before { content: "• "; }
  .value-card--energy { left: 49px; top: 54px; width: 96px; height: 74px; background: var(--energy); }
  .value-card--credibility { left: 189px; top: 54px; width: 96px; height: 74px; background: var(--credibility); }
  .value-card--relationships { left: 117px; top: 146px; width: 108px; height: 59px; background: var(--relationships); }

  .closing-title {
    position: absolute; top: 96px; width: 100%; text-align: center;
    font-family: "Tinos", "Times New Roman", serif; font-style: italic; font-weight: 700;
    font-size: 18px; line-height: 20px; color: var(--pink-text);
  }
  .closing-contact {
    position: absolute; top: 149px; width: 100%; text-align: center;
    font-size: 8px; line-height: 11px; color: var(--muted);
  }
  .closing-contact svg { width: 7px; height: 7px; vertical-align: -1px; margin-right: 2px; }
</style>
</head>
<body>
<svg width="0" height="0" style="position:absolute">
  <defs>
    <linearGradient id="band" x1="0" x2="1" y1="0" y2="0">
      <stop offset="0" stop-color="#5c0f46"/>
      <stop offset="0.55" stop-color="#9a1c73"/>
      <stop offset="1" stop-color="#e0339b"/>
    </linearGradient>
    <symbol id="footer-wave" viewBox="0 0 342 60">
      <path d="M0 6 C 30 34, 170 38, 342 22 L342 27 C 200 40, 80 44, 0 30 Z" fill="#d9d9d9"/>
      <path d="M0 34 C 110 48, 230 36, 342 28 L342 60 L0 60 Z" fill="url(#band)"/>
    </symbol>
    <symbol id="tick-box" viewBox="0 0 10 10">
      <rect x="0.5" y="0.5" width="9" height="9" fill="none" stroke="#666" stroke-width="0.9"/>
      <path d="M2 5 L4.3 7.5 L8.5 1.5" fill="none" stroke="#444" stroke-width="1.2"/>
    </symbol>
  </defs>
</svg>

<!-- Cover -->
<section class="slide slide--cover slide--r1 slide--c1">
  <div class="cover-brand">kelOrvanta</div>
  <div class="cover-tagline">• Insight &nbsp;• Impact &nbsp;• Integrity.</div>
  <div class="cover-name">Martin Hale</div>
  <div class="cover-date">July 10, 2014</div>
  <svg class="slide-footer" viewBox="0 0 342 60"><use href="#footer-wave"/></svg>
  <div class="footer-text"><span>© kelOrvanta Ltd. 2014 All Rights Reserved</span><span class="footer-url">www.kelorvanta.co.uk</span></div>
</section>

<!-- Profile -->
<section class="slide slide--r1 slide--c2">
  <header class="slide-header"><h2 class="slide-title">Martin Hale</h2>
    <div class="brand-strip"><span>• Insight &nbsp;• Impact &nbsp;• Integrity.</span><span class="brand-name">kelOrvanta</span></div></header>
  <ul class="tick-list tick-list--profile">
    <li><svg class="tick"><use href="#tick-box"/></svg>Managing Director Corvane UK</li>
    <li><svg class="tick"><use href="#tick-box"/></svg>CEO Brightway Health Co</li>
    <li><svg class="tick"><use href="#tick-box"/></svg>Managing Director Medical and Scientific</li>
    <li><svg class="tick"><use href="#tick-box"/></svg><span>Director Veltrix Market<br>Access/HE/BD/NPP/BI/Training/GA/PA/KAM</span></li>
  </ul>
  <svg class="slide-footer" viewBox="0 0 342 60"><use href="#footer-wave"/></svg>
  <div class="footer-text"><span>© kelOrvanta Ltd. 2014 All Rights Reserved</span><span class="footer-url">www.kelorvanta.co.uk</span></div>
</section>

<!-- Mission -->
<section class="slide slide--r1 slide--c3">
  <header class="slide-header"><h2 class="slide-title">Mission</h2>
    <div class="brand-strip"><span>• Insight &nbsp;• Impact &nbsp;• Integrity.</span><span class="brand-name">kelOrvanta</span></div></header>
  <p class="mission-text">Deliver Cutting Edge Performance With Our Clients<br>Through The Best Relationships With Customers That<br>Influence Access To Products And Services</p>
  <svg class="slide-footer" viewBox="0 0 342 60"><use href="#footer-wave"/></svg>
  <div class="footer-text"><span>© kelOrvanta Ltd. 2014 All Rights Reserved</span><span class="footer-url">www.kelorvanta.co.uk</span></div>
</section>

<!-- Values -->
<section class="slide slide--r2 slide--c1">
  <header class="slide-header"><h2 class="slide-title">Values</h2>
    <div class="brand-strip"><span>• Insight &nbsp;• Impact &nbsp;• Integrity.</span><span class="brand-name">kelOrvanta</span></div></header>
  <div class="value-card value-card--energy"><h3>Energy</h3><ul><li>Intensity</li><li>Fun</li><li>Determination</li><li>Fortitude</li></ul></div>
  <div class="value-card value-card--credibility"><h3>Credibility</h3><ul><li>Expertise</li><li>Experience</li><li>Professional</li><li>Constant learning</li></ul></div>
  <div class="value-card value-card--relationships"><h3>Relationships</h3><ul><li>Networking</li><li>Trust</li><li>Influencing at the top</li></ul></div>
  <svg class="slide-footer" viewBox="0 0 342 60"><use href="#footer-wave"/></svg>
  <div class="footer-text"><span>© kelOrvanta Ltd. 2014 All Rights Reserved</span><span class="footer-url">www.kelorvanta.co.uk</span></div>
</section>

<!-- Proposition -->
<section class="slide slide--r2 slide--c2">
  <header class="slide-header"><h2 class="slide-title">Proposition</h2>
    <div class="brand-strip"><span>• Insight &nbsp;• Impact &nbsp;• Integrity.</span><span class="brand-name">kelOrvanta</span></div></header>
  <ul class="tick-list tick-list--proposition">
    <li><svg class="tick"><use href="#tick-box"/></svg>Halcyon Director Team</li>
    <li><svg class="tick"><use href="#tick-box"/></svg>Halcyon Academy</li>
    <li><svg class="tick"><use href="#tick-box"/></svg>Value Proposition Build</li>
  </ul>
  <svg class="slide-footer" viewBox="0 0 342 60"><use href="#footer-wave"/></svg>
  <div class="footer-text"><span>© kelOrvanta Ltd. 2014 All Rights Reserved</span><span class="footer-url">www.kelorvanta.co.uk</span></div>
</section>

<!-- Closing -->
<section class="slide slide--r2 slide--c3">
  <header class="slide-header"><span></span>
    <div class="brand-strip"><span>• Insight &nbsp;• Impact &nbsp;• Integrity.</span><span class="brand-name">kelOrvanta</span></div></header>
  <h2 class="closing-title">Thank You<br>For Your Attention</h2>
  <p class="closing-contact">
    <svg viewBox="0 0 10 10"><circle cx="5" cy="5" r="4.5" fill="none" stroke="#e0208c"/><path d="M3.4 2.6 L4.4 3.8 L3.9 4.5 Q4.6 6 5.6 6.3 L6.3 5.7 L7.4 6.7 Q6.6 7.8 5.4 7.3 Q3 6.2 2.6 3.6 Z" fill="#e0208c"/></svg>123-555-0147<br>
    Street Name, City Name, State Zip Code
  </p>
  <svg class="slide-footer" viewBox="0 0 342 60"><use href="#footer-wave"/></svg>
  <div class="footer-text"><span>© kelOrvanta Ltd. 2014 All Rights Reserved</span><span class="footer-url">www.kelorvanta.co.uk</span></div>
</section>
</body>
</html>
```